New Packaging Design Project for Matcha Green Tea

**I've added an image called 'Sizing example', this is to show you the size of the label compared to the pack. Currently we are using full size labels for the pack and they are too difficult to apply.
Hi. I need a new label creating for a 100g pack of stunning organic premium grade Matcha tea.
The label needs to be 69mm by 88.9mm on the finished product and will be placed on a foil pack which is somewhat larger than the label.
Needs to include the text:
"Matcha Green Tea"
"Organic Japanese Premium Grade"
"Perfect for drinking, blending and baking"
"100g"
Attaching our logo and the KPV certification which both need to be on the label.
You can see our other products at www.leafhollowco.co.uk
You key with this product is that we need it to stand out on Bazolia. There are many, many other Matcha products in foil packs, so this needs to be a bold and fresh design. My suggestion is to test the design by editing it into a screenshot of the Bazolia search page for matcha tea to see if it stands out.
Target Market(s)
Affluent health conscious individuals. Those with busy life, such as executives or parents,. Those with an active life, such as triathletes, yoga, cyclists. Those with a aspirational life, i.e. they want to have quality in their life and they aspire to have the latest trends.
Requirements
Must have
- Stand out design. Clear, clean, crisp.
- Our green colour is #63A802 / 99 / 168 / 2. C41, M0, Y99, K34
- We also sometimes use #144400- R: 20 G: 68 B: 0
Nice to have
- Could either show how the product is used - i.e. lifestyle or just show the quality of the product.
- Could show the product in a ceremonial style bowl, a matcha latte or being blended or used for baking. Could even show all of these, so long as it doesn't look 'busy'.
Should not have
- Clutter, too many things going on.

```html
<!DOCTYPE html>
<html lang="en">
<head>
<meta charset="utf-8">
<title>Leafhollow Organic Matcha Label</title>
<link href="https://fonts.googleapis.com/css2?family=Cinzel:wght@400;500;600&family=Lato:wght@400&display=swap" rel="stylesheet">
<style>
  :root {
    --backdrop: #d6cba8;
    --brand-green: #63a802;
    --deep-green: #144400;
    --leaf-mid: #5b8f36;
    --leaf-dark: #2f5621;
    --powder: #4f6b2a;
    --bowl-dark: #262c1c;
    --label-white: #ffffff;
    --text-light: #f4f6ef;
  }
  * { margin: 0; padding: 0; box-sizing: border-box; }
  html, body {
    width: 1200px; height: 1200px; overflow: hidden;
    background: var(--backdrop);
  }
  .label {
    position: absolute;
    left: 190px; top: 72px;
    width: 820px; height: 1056px;
    overflow: hidden;
    background: var(--label-white);
  }
  .label-art {
    position: absolute; inset: 0;
    background:
      radial-gradient(ellipse 70% 28% at 35% 80%, rgba(95,125,48,0.95) 0%, rgba(79,107,42,0.7) 45%, rgba(38,44,28,0) 80%),
      radial-gradient(ellipse 60% 30% at 85% 40%, rgba(130,175,90,0.45) 0%, rgba(130,175,90,0) 70%),
      linear-gradient(180deg,
        var(--label-white) 0%,
        var(--label-white) 12%,
        #e6efdc 18%,
        #9fc078 25%,
        var(--leaf-mid) 33%,
        #3f6d2b 48%,
        var(--leaf-dark) 58%,
        var(--powder) 72%,
        #3a4a24 86%,
        var(--bowl-dark) 100%);
  }
  .brand-name {
    position: absolute; top: 95px; left: 0; width: 100%;
    text-align: center;
    font-family: 'Lato', sans-serif; font-weight: 400;
    font-size: 72px; color: var(--brand-green);
    letter-spacing: 0.5px;
  }
  .organic {
    position: absolute; top: 232px; left: 0; width: 100%;
    text-align: center;
    font-family: 'Cinzel', serif; font-weight: 400;
    font-size: 44px; letter-spacing: 34px; padding-left: 34px;
    color: var(--text-light);
  }
  .grade {
    position: absolute; top: 300px; left: 0; width: 100%;
    text-align: center;
    font-family: 'Cinzel', serif; font-weight: 500;
    font-size: 36px; color: var(--text-light);
  }
  .product-name {
    position: absolute; top: 378px; left: 0; width: 100%;
    text-align: center;
    font-family: 'Cinzel', serif; font-weight: 500;
    font-size: 132px; line-height: 1; color: var(--label-white);
    text-shadow: 0 2px 8px rgba(20,68,0,0.35);
  }
  .descriptor {
    position: absolute; top: 555px; left: 0; width: 100%;
    text-align: center;
    font-family: 'Cinzel', serif; font-weight: 500;
    font-size: 42px; color: var(--text-light);
  }
  .weight {
    position: absolute; left: 58px; top: 905px;
    font-family: 'Cinzel', serif; font-weight: 500;
    font-size: 44px; color: var(--label-white);
    text-transform: lowercase;
  }
  .cert-badge {
    position: absolute; left: 220px; top: 898px;
  }
  .usage {
    position: absolute; right: 58px; top: 900px;
    text-align: right;
    font-family: 'Lato', sans-serif; font-weight: 400;
    font-size: 30px; line-height: 1.35; color: var(--label-white);
  }
</style>
</head>
<body>
  <main class="label">
    <div class="label-art" role="img" aria-label="Photograph of fresh green tea leaves above a dark bowl heaped with bright matcha powder"></div>
    <div class="brand-name">Leafhollow</div>
    <div class="organic">ORGANIC</div>
    <div class="grade">Japanese Premium Grade</div>
    <h1 class="product-name">MATCHA</h1>
    <div class="descriptor">Green Tea Powder</div>
    <div class="weight">100g</div>
    <svg class="cert-badge" width="70" height="70" viewBox="0 0 70 70" role="img" aria-label="KPV organic certification badge">
      <circle cx="35" cy="35" r="31" fill="none" stroke="var(--label-white)" stroke-width="3"/>
    </svg>
    <div class="usage">Perfect for Drinking,<br>Blending and Baking</div>
  </main>
</body>
</html>
```